Business Card for Restaurant Vendal

This project consist of creating 2 design for business card of restaurant named Vendal.

The attached specs below are 'ONLY SUGGESTION' if you have others ideas. You are welcome to post it.

1) Restaurant Card

Adresse:
2784 Côte du Pinard Vert
Montréal (Qc) H4K 3T8

Website:
www.ven-dal.ca

Phone:
438-719-2046

2) Employee Card

Name: Lorna Pik
Title: Owner

Address:
2784 Côte du Pinard Vert
Montréal (Qc) H4K 3T8

Email:lorna@ven-dal.ca
Phone Number:438-719-2046
Cellphone Number:514-830-4162

 The attached specs are 'ONLY SUGGESTION' if you have others ideas.  You are welcome to post it.

Industry/Entity Type

Restaurant

Requirements
Must have
• UV Card Spot

To print Spot UV business cards you would have to submit 2 files for each side. The first file "base" would be your regular design file as it would have been in any other case. The 2nd file "UV mask" is a black/white file. The BLACK color will indicate the areas that will be covered with the UV high gloss finish. To upload the files, please combine front design and front mask file in one P
Nice to have
• 1) The font of the logo should be ink effect
2) black background with wallpaper effect
3) The specs below are 'ONLY SUGGESTION' if you have others ideas. You are welcome to post it.

```html
<!DOCTYPE html>
<html lang="fr">
<head>
<meta charset="utf-8">
<title>Restaurant Vendal – Business Cards</title>
<link rel="stylesheet" href="https://fonts.googleapis.com/css2?family=Jost:wght@400;500;600&family=Noto+Sans+JP:wght@400;500;700&display=swap">
<style>
  :root {
    --stage-bg: #ece8e3;
    --card-bg: #2a2829;
    --lantern-red: #ee3124;
    --ink-white: #ffffff;
    --label-ink: #1a1a1a;
    --sans: "Jost", "Futura", sans-serif;
    --jp: "Noto Sans JP", sans-serif;
  }
  * { margin: 0; padding: 0; box-sizing: border-box; }
  html, body { width: 1200px; height: 924px; overflow: hidden; }
  body { background: var(--stage-bg); position: relative; font-family: var(--sans); }

  .side-label {
    position: absolute; left: 291px; width: 619px; text-align: center;
    font-family: var(--sans); font-weight: 600; font-size: 15px; color: var(--label-ink);
  }
  .side-label--front { top: 52px; }
  .side-label--back { top: 866px; }

  .card {
    position: absolute; left: 291px; width: 619px; height: 361px;
    background: var(--card-bg); overflow: hidden; color: var(--ink-white);
  }
  .card--front { top: 98px; }
  .card--back { top: 492px; }

  .lantern { position: absolute; }
  .lantern--front { left: 0; top: 30px; width: 245px; height: 331px; }
  .lantern--back { left: 384px; top: 66px; width: 224px; height: 256px; }

  /* front */
  .brand { position: absolute; left: 278px; top: 70px; display: flex; align-items: center; gap: 10px; }
  .brand__dot { width: 14px; height: 14px; border-radius: 50%; background: var(--lantern-red); }
  .brand__name { font-family: var(--sans); font-weight: 600; font-size: 70px; line-height: 1; color: var(--ink-white); letter-spacing: 1px; }
  .brand__kana {
    position: absolute; left: 554px; top: 100px; writing-mode: vertical-rl;
    font-family: var(--jp); font-size: 19px; line-height: 1; letter-spacing: 2px;
  }
  .tagline { position: absolute; left: 293px; top: 172px; font-size: 13px; font-weight: 500; letter-spacing: .2px; }
  .tagline .jp { font-family: var(--jp); font-size: 12px; }

  .venue-info { position: absolute; left: 292px; top: 236px; font-size: 16.5px; line-height: 22px; }
  .venue-info .web { color: var(--lantern-red); }

  /* back */
  .back-kana { position: absolute; left: 96px; top: 40px; font-family: var(--jp); font-size: 30px; font-weight: 500; letter-spacing: 1px; }
  .staff { position: absolute; right: 254px; top: 98px; text-align: right; font-size: 16.5px; line-height: 22px; }
  .staff__name { font-weight: 600; }
  .staff__address { margin-top: 22px; }
  .staff .field { color: var(--lantern-red); }
  .lantern-kanji {
    position: absolute; left: 452px; top: 126px; writing-mode: vertical-rl;
    font-family: var(--jp); font-weight: 700; font-size: 44px; line-height: 1; letter-spacing: 6px; color: var(--ink-white);
  }
</style>
</head>
<body>
  <div class="side-label side-label--front">Business card : FRONT</div>

  <section class="card card--front">
    <svg class="lantern lantern--front" viewBox="0 0 245 331" role="img" aria-label="Red paper lantern illustration">
      <path d="M0 60 C60 35 150 45 205 80 C240 120 248 200 238 250 C225 300 150 331 60 331 L0 331 Z" fill="var(--lantern-red)"/>
    </svg>
    <div class="brand">
      <span class="brand__name">Vendal</span>
      <span class="brand__dot"></span>
    </div>
    <div class="brand__kana">ベンダル</div>
    <p class="tagline">Resto-Bar Japonais · Izakaya · <span class="jp">居酒屋</span></p>
    <address class="venue-info" style="font-style:normal">
      2784 Côte du Pinard Vert<br>
      Montréal (Qc) H4K 3T8<br>
      info@ven-dal.ca<br>
      <span class="web">www.ven-dal.ca</span>
    </address>
  </section>

  <section class="card card--back">
    <div class="back-kana">ベンダル</div>
    <div class="staff">
      <div class="staff__name">Lorna Pik</div>
      <div class="staff__title">Owner</div>
      <address class="staff__address" style="font-style:normal">
        2784 Côte du Pinard Vert<br>
        Montréal (Qc) H4K 3T8<br>
        www.ven-dal.ca<br>
        <span class="field">Phone :</span> 438-719-2046<br>
        <span class="field">Email :</span> lorna@ven-dal.ca<br>
        <span class="field">Cellphone :</span> 514-830-4162
      </address>
    </div>
    <svg class="lantern lantern--back" viewBox="0 0 224 256" role="img" aria-label="Red paper lantern illustration">
      <path d="M40 40 C90 20 160 25 195 50 C225 90 228 170 212 205 C190 245 140 256 100 254 C50 250 10 225 4 175 C-2 120 8 65 40 40 Z" fill="var(--lantern-red)"/>
    </svg>
    <div class="lantern-kanji">居酒屋</div>
  </section>

  <div class="side-label side-label--back">Business card : BACK</div>
</body>
</html>
```